Verodex business card

Business card for sustainable investment company called "Verodex". Verodex is an exchange platform selling carbon credits between buyers and sellers. Carbon Credits are an environmental commodity for reducing global carbon emissions.

the card should obviously have our logo and the theme should be sustainability/environment mixed with a trading platform.

Contact Information for Business Card

Logo, Name, Title, Phone, Email

Colors
0054AA
0677BA
7BADD7
CADEEF
E8F1F8
0094D4
00A9DD
6FCCEA
C7EBF8
E9F6FB
00AB8E
00BBA5
67D7C9
C6EFE9
E9F9F6
59FF00
82FF00
B8FF75
E3FFCB
F4FFEA

```html
<!DOCTYPE html>
<html lang="en">
<head>
<meta charset="utf-8">
<title>Verodex business card</title>
<link rel="stylesheet" href="https://fonts.googleapis.com/css2?family=Oswald:wght@700&family=Arimo:wght@400;700&display=swap">
<style>
  :root {
    --backdrop: #cadeef;
    --card-light: #e9f6fb;
    --card-deep: #0054aa;
    --edge-light: #7badd7;
    --edge-deep: #003f80;
    --ink: #0054aa;
    --ink-soft: #0677ba;
    --leaf: #00ab8e;
    --spark: #82ff00;
    --on-deep: #e9f6fb;
  }
  * { margin: 0; padding: 0; box-sizing: border-box; }
  html, body { width: 1200px; height: 976px; overflow: hidden; }
  body {
    background: var(--backdrop);
    font-family: "Arimo", Arial, sans-serif;
    color: var(--ink);
    position: relative;
  }
  .card {
    position: absolute;
    left: 250px;
    width: 700px;
    height: 400px;
  }
  .card--front {
    top: 64px;
    background: var(--card-light);
    border-bottom: 4px solid var(--edge-light);
  }
  .card--back {
    top: 512px;
    background: var(--card-deep);
    border-bottom: 4px solid var(--edge-deep);
    color: var(--on-deep);
  }

  .identity {
    position: absolute;
    right: 370px;
    top: 150px;
    text-align: right;
  }
  .identity__name {
    font-family: "Oswald", "Arial Narrow", sans-serif;
    font-weight: 700;
    font-size: 34px;
    letter-spacing: 1.5px;
    line-height: 1;
    color: var(--ink);
  }
  .identity__title {
    font-size: 18px;
    letter-spacing: 1px;
    margin-top: 6px;
    color: var(--ink-soft);
  }
  .divider {
    position: absolute;
    left: 350px;
    top: 150px;
    width: 2px;
    height: 100px;
    background: var(--leaf);
  }
  .contact {
    position: absolute;
    left: 376px;
    top: 156px;
    list-style: none;
    font-weight: 700;
    font-size: 17px;
    line-height: 1.45;
    letter-spacing: 0.5px;
    color: var(--ink);
  }
  .contact__phone { font-size: 21px; }

  .brand {
    position: absolute;
    display: flex;
    align-items: center;
    gap: 10px;
    font-weight: 700;
  }
  .brand--small { top: 56px; right: 56px; font-size: 22px; color: var(--ink); }
  .brand--small .brand__mark { width: 14px; height: 14px; background: var(--leaf); }
  .brand--large {
    top: 50%; left: 50%;
    transform: translate(-50%, -50%);
    font-size: 78px;
    letter-spacing: 2px;
    gap: 22px;
    color: var(--on-deep);
  }
  .brand--large .brand__mark { width: 48px; height: 48px; background: var(--spark); }
</style>
</head>
<body>
  <section class="card card--front">
    <div class="identity">
      <h1 class="identity__name">MARCUS HALE</h1>
      <p class="identity__title">Founder &amp; CEO</p>
    </div>
    <div class="divider"></div>
    <ul class="contact">
      <li class="contact__phone">(555) 014-2290</li>
      <li>office@verodex.com</li>
      <li>verodex.com</li>
    </ul>
    <div class="brand brand--small"><span class="brand__mark"></span><span>Verodex</span></div>
  </section>

  <section class="card card--back">
    <div class="brand brand--large"><span class="brand__mark"></span><span>Verodex</span></div>
  </section>
</body>
</html>
```